Spring Camp flyer

I would like a postcard that promotes our Spring Break Camp, with normal postcard design on reverse side. The target age group for our camp is between 2 and 7 years old, it needs to be very visually appealing and exciting! Vibrant and quite cool so that people want to pick it up and see what it is :)
I love the file titled SpringBrk a lot!
I also need the details
www.zelvanoro.ae
info@zelvanoro.ae
Camp is 800 aed per week
1200 for both weeks
9am - 2pm with early drop and late pick up available
Um Suqeim 3 location
Daily activities include;
yoga, brain training, language, creative arts, sports and more!
Online gallery updated daily!

```html
<!DOCTYPE html>
<html lang="en">
<head>
<meta charset="utf-8">
<title>Spring Break Camp Postcard</title>
<link rel="stylesheet" href="https://fonts.googleapis.com/css2?family=Arvo:ital,wght@0,400;0,700;1,400;1,700&family=Lato:ital,wght@0,400;0,700;0,900;1,400;1,700&display=swap">
<style>
  :root {
    --backdrop: #8f5fb3;
    --sun-core: #fff6a8;
    --sun-mid: #ffe04a;
    --sun-edge: #f7b52a;
    --headline: #e8511f;
    --teal: #3fa9b0;
    --teal-dark: #1f7c86;
    --cream: #fff3c4;
    --navy: #1c3f7a;
    --info-red: #c8361f;
    --bar-blue: #1d6fc1;
    --blob-orange: #f08a24;
    --white: #ffffff;
  }
  * { box-sizing: border-box; margin: 0; padding: 0; }
  html, body { width: 791px; height: 1200px; overflow: hidden; }
  body { background: var(--backdrop); font-family: "Lato", sans-serif; position: relative; }

  .card { position: absolute; left: 45px; width: 701px; overflow: hidden; background: var(--white); }
  .card--front { top: 40px; height: 553px;
    background: radial-gradient(circle at 50% 40%, var(--sun-core) 0%, var(--sun-mid) 40%, var(--sun-edge) 100%); }
  .card--back { top: 614px; height: 546px; }

  .brand { position: absolute; left: 24px; top: 16px; display: flex; align-items: center; gap: 8px;
    background: var(--white); padding: 8px 12px; border-radius: 6px; }
  .brand__dot { width: 18px; height: 18px; border-radius: 50%; background: var(--teal); }
  .brand__name { font-weight: 900; font-size: 17px; color: var(--navy); }

  .headline { position: absolute; left: 170px; right: 20px; top: 14px; text-align: center;
    font-family: "Arvo", serif; font-weight: 700; font-size: 50px; line-height: 1.2; color: var(--headline);
    text-shadow: 2px 2px 0 #fff6d0; }

  .banner { position: absolute; left: 120px; top: 120px; width: 460px; height: 160px; }
  .banner svg { position: absolute; inset: 0; }
  .banner__title { position: absolute; left: 0; right: 0; top: 22px; text-align: center;
    font-family: "Arvo", serif; font-weight: 700; font-size: 30px; line-height: 1.2; color: var(--cream); white-space: nowrap; }
  .banner__dates { position: absolute; left: 0; right: 0; top: 76px; text-align: center;
    font-weight: 900; font-size: 22px; line-height: 1.2; color: var(--white); }
  .banner__hours { position: absolute; left: 0; right: 0; top: 106px; text-align: center;
    font-weight: 900; font-size: 20px; line-height: 1.2; color: var(--white); }
  .care-note { position: absolute; left: 0; right: 0; top: 290px; text-align: center;
    font-style: italic; font-weight: 700; font-size: 15px; color: var(--navy); }

  .price { position: absolute; width: 112px; height: 112px; border-radius: 50%;
    background: var(--teal); border: 4px solid var(--white); color: var(--white);
    display: flex; align-items: center; justify-content: center; text-align: center;
    font-weight: 900; font-size: 16px; line-height: 1.2; padding: 10px; }
  .price--week { left: 18px; top: 270px; }
  .price--both { right: 18px; top: 290px; }

  .details { position: absolute; left: 0; right: 0; top: 320px; text-align: center; color: var(--navy); }
  .details__hours { width: 400px; margin: 0 auto; font-weight: 900; font-size: 21px; line-height: 1.3; }
  .details__place { font-weight: 900; font-size: 21px; line-height: 1.3; }
  .details__lead { font-style: italic; font-weight: 700; font-size: 18px; line-height: 1.3; margin-top: 4px; color: var(--info-red); }
  .details__list { font-weight: 900; font-size: 17px; line-height: 1.3; margin-top: 2px; }

  .info { position: absolute; left: 0; right: 0; bottom: 0; }
  .info__note { background: var(--white); text-align: center; font-family: "Arvo", serif;
    font-style: italic; font-weight: 700; font-size: 15px; color: var(--info-red); padding: 6px 0; }
  .info__bar { background: var(--bar-blue); color: var(--white); display: flex; justify-content: space-around;
    align-items: center; font-weight: 900; font-size: 17px; padding: 8px 12px; }
  .info__item { display: flex; align-items: center; gap: 6px; }
  .info__icon { width: 16px; height: 16px; }

  .collage { position: absolute; left: 0; top: 0; width: 701px; height: 470px;
    background: linear-gradient(135deg, #e9dccb 0%, #cfa98a 30%, #e3e6ee 55%, #b9c6d8 75%, #efd7c2 100%); }
  .activities-blob { position: absolute; left: 175px; top: 110px; width: 380px; height: 230px; }
  .activities-blob svg { position: absolute; inset: 0; }
  .activities-blob__text { position: absolute; inset: 30px 38px; display: flex; align-items: center;
    justify-content: center; text-align: center; font-family: "Arvo", serif; font-weight: 700;
    font-size: 27px; line-height: 1.22; color: var(--white); }
</style>
</head>
<body>

<section class="card card--front">
  <div class="brand"><span class="brand__dot"></span><span class="brand__name">Zelvanoro</span></div>
  <h1 class="headline">Step Right Up !</h1>

  <div class="banner">
    <svg viewBox="0 0 460 160" width="460" height="160">
      <polygon points="0,26 34,16 34,78 0,88 16,57" fill="var(--teal-dark)"/>
      <polygon points="460,26 426,16 426,78 460,88 444,57" fill="var(--teal-dark)"/>
      <path d="M28 12 Q230 -4 432 12 L432 150 Q230 136 28 150 Z" fill="var(--teal)" stroke="var(--white)" stroke-width="3"/>
    </svg>
    <div class="banner__title">SPRING BREAK CAMP</div>
    <div class="banner__dates">March 23-27</div>
    <div class="banner__hours">9 am - 3 pm</div>
  </div>
  <p class="care-note">before and after care is available</p>

  <div class="price price--week">Camp is 800 aed per week</div>
  <div class="price price--both">1200 for both weeks</div>

  <div class="details">
    <p class="details__hours">9am - 2pm with early drop and late pick up available</p>
    <p class="details__place">Um Suqeim 3 location</p>
    <p class="details__lead">Daily activities include;</p>
    <p class="details__list">yoga, brain training, language, creative arts, sports and more!</p>
  </div>

  <div class="info">
    <p class="info__note">For more information please contact director of activities</p>
    <div class="info__bar">
      <span class="info__item">www.zelvanoro.ae</span>
      <span class="info__item">
        <svg class="info__icon" viewBox="0 0 16 16"><rect x="1" y="3" width="14" height="10" fill="none" stroke="#fff" stroke-width="1.6"/><polyline points="1,3 8,9 15,3" fill="none" stroke="#fff" stroke-width="1.6"/></svg>
        info@zelvanoro.ae</span>
      <span class="info__item">
        <svg class="info__icon" viewBox="0 0 16 16"><path d="M3 1 L6 1 L7 5 L5 6.5 Q6.5 9.5 9.5 11 L11 9 L15 10 L15 13 Q15 15 13 15 Q1 14 1 3 Q1 1 3 1 Z" fill="#fff"/></svg>
        +9714 555 0192</span>
    </div>
  </div>
</section>

<section class="card card--back">
  <div class="collage" role="img" aria-label="Collage of photos of young children doing crafts, painting and playing together at camp"></div>
  <div class="activities-blob">
    <svg viewBox="0 0 380 230" width="380" height="230">
      <path d="M40 60 Q30 10 110 18 Q190 -8 270 16 Q360 10 358 80 Q390 140 340 185 Q280 232 190 218 Q90 235 40 190 Q-10 140 40 60 Z" fill="var(--blob-orange)"/>
    </svg>
    <p class="activities-blob__text">Daily activities include; yoga, brain training language, creative arts sports and more!</p>
  </div>

  <div class="info">
    <p class="info__note">For more information please contact director of activities</p>
    <div class="info__bar">
      <span class="info__item">www.zelvanoro.ae</span>
      <span class="info__item">
        <svg class="info__icon" viewBox="0 0 16 16"><rect x="1" y="3" width="14" height="10" fill="none" stroke="#fff" stroke-width="1.6"/><polyline points="1,3 8,9 15,3" fill="none" stroke="#fff" stroke-width="1.6"/></svg>
        info@zelvanoro.ae</span>
      <span class="info__item">
        <svg class="info__icon" viewBox="0 0 16 16"><path d="M3 1 L6 1 L7 5 L5 6.5 Q6.5 9.5 9.5 11 L11 9 L15 10 L15 13 Q15 15 13 15 Q1 14 1 3 Q1 1 3 1 Z" fill="#fff"/></svg>
        +9714 555 0192</span>
    </div>
  </div>
</section>

</body>
</html>
```